依頼概要
弊社はクレジットカードの比較サイトを運営しています。
サイトリニューアルにあたり、下記テキスト(15項目)を使ったアイコンの作成をお願いします。

1.おすすめ
2.年会費無料
3.初年度年会費無料
4.スピード発行
5.ETC一体型
6.学生専用カード
7.女性向けカード
8.リボ払い専用カード
9.プレミアムカード
10.ブラックカード
11.プラチナカード
12.ゴールドカード
13.ヤングゴールドカード
14.格安ゴールドカード
15.スタンダードカード

《グループ1》
おすすめ

《グループ2》
年会費無料、初年度年会費無料

《グループ3》
スピード発行

《グループ4》
ETC一体型、学生専用カード、女性向けカード、リボ払い専用カード、
プレミアムカード、ブラックカード、プラチナカード、ゴールドカード、
ヤングゴールドカード、格安ゴールドカード、スタンダードカード

アイコンの縦サイズは全て26pxでお願いします。
限られたスペースに表示させていくため横幅が限られています。
同時に表示させるアイコンは最大で4つです。
その際の横幅は230pxで収まるようにしてください。
アイコンとアイコンの間には4pxずつ隙間を入れるので
4つのアイコンで実際に使える幅は218pxです。

```html
<!DOCTYPE html>
<html lang="ja">
<head>
<meta charset="utf-8">
<title>カード特徴アイコン一覧</title>
<link rel="stylesheet" href="https://fonts.googleapis.com/css2?family=M+PLUS+Rounded+1c:wght@500;800&display=swap">
<style>
:root{
  --bg:#ffffff;
  --row:#e9eff8;
  --row-line:#d3dceb;
  --white:#ffffff;
  --recommend-a:#ffd21a; --recommend-b:#f28a00;
  --free-a:#e8401c; --free-b:#9c1a08;
  --speed-a:#6fb6ff; --speed-b:#2f63c9;
  --etc-a:#8c48d8; --etc-b:#4a1a8e;
  --student-a:#eaf7e0; --student-b:#b8e09a; --student-text:#2e8b1e;
  --ladies-a:#ff9ad0; --ladies-b:#e2308e;
  --revo-a:#3aa12b; --revo-b:#c06b00;
  --premium-a:#5a5a5a; --premium-b:#111111;
  --black-a:#2a2a2a; --black-b:#000000;
  --platinum-a:#ffffff; --platinum-b:#bdbdbd; --platinum-text:#7a7a7a;
  --gold-a:#f6e27a; --gold-b:#c9a20f;
  --young-a:#f6e27a; --young-b:#d6a400;
  --cheap-a:#f6e27a; --cheap-b:#d6a400; --cheap-text:#e0246e;
  --standard-a:#d8f4fb; --standard-b:#8fd3ea; --standard-text:#3a8fb5;
  --coin:#f3c21a; --coin-text:#8a4b00;
}
*{box-sizing:border-box;margin:0;padding:0}
html,body{width:900px;height:1200px;overflow:hidden;background:var(--bg)}
body{font-family:"M PLUS Rounded 1c",sans-serif;position:relative}
.icon{position:absolute;height:78px;border-radius:6px;display:flex;align-items:center;justify-content:center;
  text-align:center;font-weight:800;color:var(--white);line-height:1.05;letter-spacing:1px;white-space:nowrap;
  box-shadow:0 2px 3px rgba(0,0,0,.25);text-shadow:0 0 3px rgba(0,0,0,.55)}
.top-row .icon{top:45px}
.grid{position:absolute;left:96px;top:144px;width:690px}
.grid-row{position:relative;height:99px;margin-bottom:3px;background:var(--row);border-bottom:2px solid var(--row-line)}
.grid-row::after{content:"";position:absolute;left:489px;top:0;bottom:0;width:2px;background:var(--bg)}
.grid-row .icon{top:10px}
.cell-right{left:492px;width:162px}
.coin{position:absolute;width:32px;height:32px;border-radius:50%;background:var(--coin);color:var(--coin-text);
  font-size:13px;display:flex;align-items:center;justify-content:center;text-shadow:none;top:4px;right:10px;letter-spacing:0}
.recommend{left:111px;width:129px;background:linear-gradient(var(--recommend-a),var(--recommend-b));font-size:26px;color:#c8002a;text-shadow:0 0 3px #fff}
.free{left:249px;width:171px;background:linear-gradient(var(--free-a),var(--free-b));font-size:23px;padding-top:26px}
.speed{left:429px;width:150px;background:linear-gradient(var(--speed-a),var(--speed-b));font-size:23px}
.etc{left:588px;width:162px;background:linear-gradient(135deg,var(--etc-a),var(--etc-b));font-size:24px}
.first-free{left:153px;width:171px;background:linear-gradient(var(--free-a),var(--free-b));font-size:21px}
.student{background:linear-gradient(var(--student-a),var(--student-b));color:var(--student-text);text-shadow:none;font-size:23px}
.ladies{background:linear-gradient(var(--ladies-a),var(--ladies-b));font-size:23px}
.revo{background:linear-gradient(90deg,var(--revo-a),var(--revo-b));font-size:22px}
.premium{background:linear-gradient(var(--premium-a),var(--premium-b));font-size:22px}
.black{background:linear-gradient(var(--black-a),var(--black-b));font-size:24px}
.platinum{background:linear-gradient(var(--platinum-a),var(--platinum-b));color:var(--platinum-text);text-shadow:none;font-size:23px}
.gold{background:linear-gradient(var(--gold-a),var(--gold-b));font-size:23px}
.young{background:linear-gradient(var(--young-a),var(--young-b));font-size:19px;letter-spacing:0}
.cheap{background:linear-gradient(var(--cheap-a),var(--cheap-b));color:var(--cheap-text);text-shadow:0 0 3px #fff;font-size:21px;letter-spacing:0}
.standard{background:linear-gradient(var(--standard-a),var(--standard-b));font-size:21px;letter-spacing:0;color:var(--standard-text);text-shadow:0 0 2px #fff}
</style>
</head>
<body>
<div class="top-row">
  <div class="icon recommend">おすすめ</div>
  <div class="icon free"><span class="coin">¥0</span>年会費無料</div>
  <div class="icon speed">スピード<br>発行</div>
  <div class="icon etc">ETC<br>一体型</div>
</div>
<div class="grid">
  <div class="grid-row">
    <div class="icon first-free">初年度<br>年会費無料</div>
    <div class="icon cell-right student">学生専用<br>カード</div>
  </div>
  <div class="grid-row"><div class="icon cell-right ladies">女性向け<br>カード</div></div>
  <div class="grid-row"><div class="icon cell-right revo">リボ払い<br>専用カード</div></div>
  <div class="grid-row"><div class="icon cell-right premium">プレミアム<br>カード</div></div>
  <div class="grid-row"><div class="icon cell-right black">ブラック<br>カード</div></div>
  <div class="grid-row"><div class="icon cell-right platinum">プラチナ<br>カード</div></div>
  <div class="grid-row"><div class="icon cell-right gold">ゴールド<br>カード</div></div>
  <div class="grid-row"><div class="icon cell-right young">ヤングゴールド<br>カード</div></div>
  <div class="grid-row"><div class="icon cell-right cheap">激安ゴールド<br>カード</div></div>
  <div class="grid-row"><div class="icon cell-right standard">スタンダード<br>カード</div></div>
</div>
</body>
</html>
```